Real Estate Sign 24" wide X 36" long

We are looking for creative modern design for a real estate sign, Wow us but remember its about people driving by the sign and retaining our brand.

The Brisket Hollow Logo need to be at the bottom of sign. Please use change colors to fit your design.

Also need the following on the sign:

555.380.4162
Lev Marchetti Piers Okafor
Marchetti & Okafor Logo
Lev and Piers's picture

Our current sign we are replacing is attached: "Pemberly M&O". We are replacing for more modern beautiful design that is one piece.

A rough draft is also attached...but be creative...don't think inside a box.

Target Market(s)

Home Buyers and Sellers

Industry/Entity Type

Real Estate Agent

Colors

Designer to choose colors to be used in the design.

Requirements
Must have
• The sign must be 24" wide X 36" tall. This will be the sign we hang in front of homes for sale.
Nice to have
• Background design that works well would be nice.
• Our business is in Florida...would be nice to have background palm trees, sun, beach...but not necessary.

```html
<!DOCTYPE html>
<html lang="en">
<head>
<meta charset="utf-8">
<title>Open House Sign – Marchetti &amp; Okafor</title>
<link rel="stylesheet" href="https://fonts.googleapis.com/css2?family=EB+Garamond:wght@700&family=Open+Sans:wght@700;800&display=swap">
<style>
  :root {
    --sign-blue: #2395e0;
    --sign-blue-deep: #1f88d2;
    --sign-blue-light: #6bb7ea;
    --sign-blue-mid: #4aa6e6;
    --white: #ffffff;
    --agent-yellow: #eeea34;
    --ink: #242424;
  }
  html, body {
    margin: 0;
    padding: 0;
    width: 1200px;
    height: 900px;
    overflow: hidden;
    background: var(--sign-blue);
  }
  .sign {
    position: relative;
    width: 1200px;
    height: 900px;
    overflow: hidden;
    background: var(--sign-blue);
    font-family: "Open Sans", Arial, sans-serif;
  }
  .sign-backdrop {
    position: absolute;
    inset: 0;
  }
  .team-name {
    position: absolute;
    top: 150px;
    left: 0;
    width: 1200px;
    text-align: center;
    color: var(--white);
    font-weight: 700;
    font-size: 58px;
    letter-spacing: 1px;
    margin: 0;
  }
  .phone {
    position: absolute;
    top: 286px;
    left: 0;
    width: 1200px;
    text-align: center;
    color: var(--white);
    font-weight: 800;
    font-size: 128px;
    line-height: 1;
    letter-spacing: 2px;
    margin: 0;
  }
  .agents {
    position: absolute;
    top: 430px;
    left: 0;
    width: 1200px;
    display: flex;
    justify-content: center;
    align-items: center;
    gap: 14px;
    color: var(--agent-yellow);
    font-weight: 700;
    font-size: 44px;
    line-height: 1;
    letter-spacing: -0.5px;
  }
  .agents-divider {
    width: 3px;
    height: 46px;
    background: var(--agent-yellow);
  }
  .open-house-arrow {
    position: absolute;
    inset: 0;
  }
  .open-house-label {
    font-family: "EB Garamond", Georgia, serif;
    font-weight: 700;
    font-size: 120px;
    fill: var(--ink);
  }
  .brokerage-name {
    position: absolute;
    right: 36px;
    bottom: 30px;
    color: var(--white);
    font-family: "EB Garamond", Georgia, serif;
    font-weight: 700;
    font-size: 38px;
    letter-spacing: 1px;
    margin: 0;
  }
</style>
</head>
<body>
<main class="sign">
  <svg class="sign-backdrop" width="1200" height="900" viewBox="0 0 1200 900" aria-hidden="true">
    <path d="M0 0 H220 C120 60 30 170 0 260 Z" fill="var(--sign-blue-light)"/>
    <path d="M220 0 H420 C230 30 60 160 0 330 V260 C30 170 120 60 220 0 Z" fill="var(--sign-blue-mid)"/>
    <path d="M0 848 C420 850 900 770 1200 640 V900 H0 Z" fill="var(--sign-blue-deep)"/>
  </svg>

  <p class="team-name">Marchetti &amp; Okafor</p>

  <p class="phone">555.380.4162</p>

  <div class="agents">
    <span class="agent">Lev Marchetti</span>
    <span class="agents-divider"></span>
    <span class="agent">Piers Okafor</span>
  </div>

  <svg class="open-house-arrow" width="1200" height="900" viewBox="0 0 1200 900">
    <polygon points="61,513 1012,513 1012,462 1141,586 1012,706 1012,658 61,658 114,586" fill="var(--white)"/>
    <text class="open-house-label" x="220" y="628" textLength="762" lengthAdjust="spacingAndGlyphs">OPEN HOUSE</text>
  </svg>

  <p class="brokerage-name">Brisket Hollow</p>
</main>
</body>
</html>
```